Air Conditioning Advertisement

I am looking to design an ad for my HVAC company. The name of my company is Silver Pine Cooling INC. We provide 24/7 emergency service.
Image- Ductless air conditioning unit & central air conditioning unit
Website- www.pinebreezehvac.example
company phone number- 555-387-9042

I would like an ad advertising our spring special. The spring special is $750 off a new Central Air conditioning or ductlesss air conditioning installation.

Our other special is $100 Central AC Tune up.

I attached my logo.

Target Market(s)

Home owners & small businesses

Industry/Entity Type

Air conditioning, Refrigeration & Heating

Colors
0054AA
0677BA
7BADD7
CADEEF
E8F1F8
EE7325
F08F49
F5BC92
FAE3D3
FDF4ED

Requirements
Must have
• Pictures of ductless air conditioning and central air conditioning unit.
Nice to have
• Id like to have an ad that incorporates my company colors & logos. I want this ad to stand out & show what we are offering. The ad should display, briefly say the importance of comfort in your home.

```html
<!DOCTYPE html>
<html lang="en">
<head>
<meta charset="utf-8">
<title>Silver Pine Cooling – Spring Special Ads</title>
<link rel="stylesheet" href="https://fonts.googleapis.com/css2?family=Pacifico&family=Roboto+Condensed:ital,wght@0,400;0,700;1,700&family=Montserrat:ital,wght@0,300;0,700;0,800;0,900;1,800;1,900&display=swap">
<style>
  :root{
    --board-grey:#b3b3b3;
    --brand-blue:#0a4ec2;
    --mid-blue:#3a82dc;
    --sky-blue:#7badd7;
    --pale-blue:#cadeef;
    --mist-blue:#e8f1f8;
    --orange:#ff6600;
    --ink:#111;
    --white:#fff;
  }
  *{box-sizing:border-box;margin:0;padding:0}
  html,body{width:1200px;height:953px;overflow:hidden;background:var(--white)}
  body{position:relative;font-family:"Roboto Condensed",Arial,sans-serif;color:var(--ink)}

  .board{position:absolute;left:0;top:0;width:1200px;height:478px;background:var(--board-grey)}
  .board-title{position:absolute;top:22px;width:100%;text-align:center;font-family:"Montserrat",sans-serif;font-weight:300;font-size:26px;letter-spacing:17px;color:var(--white)}

  .ad{position:absolute;top:81px;width:328px;height:328px;overflow:hidden;background:var(--white);box-shadow:0 6px 14px rgba(0,0,0,.35)}
  .ad > *{position:absolute}
  .ad-one{left:54px}
  .ad-two{left:436px;background:var(--mid-blue)}
  .ad-three{left:820px}

  .bg-shapes{left:0;top:0;width:100%;height:100%}

  .spring{font-family:"Pacifico",cursive;color:var(--brand-blue);line-height:1;white-space:nowrap}
  .special{font-family:"Roboto Condensed",sans-serif;font-weight:700;color:var(--orange);line-height:1}

  .unit-photo{background:radial-gradient(ellipse at 55% 55%,#f4f6f8 0 38%,#d5dbe2 48%,var(--sky-blue) 62%,rgba(123,173,215,0) 75%)}
  .ceiling-photo{background:radial-gradient(ellipse at 50% 50%,#eef1f4 0 40%,#c3c9d0 58%,rgba(255,255,255,0) 72%)}

  .badge{border-radius:50%;background:var(--orange);color:var(--white);display:flex;flex-direction:column;align-items:center;justify-content:center;transform:rotate(-28deg);line-height:.95}
  .badge .amount{font-family:"Roboto Condensed",sans-serif;font-weight:400}
  .badge .off{font-family:"Montserrat",sans-serif;font-weight:900}

  .offer{font-size:12px;line-height:15px}
  .right{text-align:right}

  .brand{display:flex;align-items:center;gap:6px}
  .brand-dot{flex:none;border-radius:50%;background:var(--orange)}
  .brand-name{font-family:"Montserrat",sans-serif;font-weight:800;color:var(--brand-blue);line-height:1.02}

  .tune-up{font-family:"Montserrat",sans-serif;font-style:italic;font-weight:800}
  .phone{font-family:"Montserrat",sans-serif;font-style:italic;font-weight:900;color:var(--orange);white-space:nowrap}
  .site{font-family:"Montserrat",sans-serif;font-style:italic;font-weight:900;color:var(--brand-blue);white-space:nowrap}
  .caps{font-family:"Roboto Condensed",sans-serif;font-weight:700;text-transform:uppercase;white-space:nowrap}

  /* banner */
  .banner{position:absolute;left:86px;top:574px;width:1042px;height:334px;border:1.5px solid #9a9a9a;overflow:hidden;background:var(--white)}
  .banner > *{position:absolute}
  .estimate-band{left:476px;top:286px;width:570px;height:48px;background:var(--orange);clip-path:polygon(47px 0,100% 0,100% 100%,0 100%)}
  .service-line{left:24px;top:294px;font-family:"Montserrat",sans-serif;font-weight:700;font-size:19px;white-space:nowrap;color:var(--ink)}
</style>
</head>
<body>

<section class="board">
  <h1 class="board-title">FACEBOOK ADD</h1>

  <!-- Ad one -->
  <article class="ad ad-one">
    <svg class="bg-shapes" viewBox="0 0 328 328" aria-hidden="true">
      <path d="M0 218 C80 260 200 262 328 190 L328 328 L0 328Z" fill="var(--sky-blue)"/>
      <path d="M0 226 C80 272 210 272 328 205 L328 328 L0 328Z" fill="var(--mid-blue)"/>
      <rect x="0" y="285" width="328" height="26" fill="var(--white)"/>
      <rect x="0" y="311" width="328" height="6" fill="var(--pale-blue)"/>
    </svg>
    <div class="unit-photo" role="img" aria-label="Ceiling cassette and ductless wall-mounted air conditioning units on a blue splash" style="left:168px;top:22px;width:165px;height:150px"></div>
    <div class="spring" style="left:28px;top:4px;font-size:52px">Spring</div>
    <div class="special" style="left:70px;top:76px;font-size:18px">SPECIAL</div>
    <div class="badge" style="left:244px;top:10px;width:72px;height:72px"><span class="amount" style="font-size:20px">$750</span><span class="off" style="font-size:12px">OFF</span></div>
    <p class="offer right" style="left:10px;top:108px;width:171px">New Central Air conditioning or Ductlesss air conditioning installation.</p>
    <div class="brand" style="left:38px;top:180px"><span class="brand-dot" style="width:32px;height:32px"></span><span class="brand-name" style="font-size:17px">Silver Pine<br>Cooling</span></div>
    <p class="tune-up right" style="left:210px;top:168px;width:103px;font-size:8.5px;line-height:10.5px">Our other<br>special is a $100<br>Central AC Tune up.</p>
    <p class="caps" style="left:0;width:328px;top:266px;text-align:center;font-size:14px;color:var(--white)">We provide 24/7 emergency service.</p>
    <p class="phone" style="left:0;width:328px;top:289px;text-align:center;font-size:13px">Free Estimates Call Us 555-387-9042</p>
    <p class="site" style="left:0;width:328px;top:309px;text-align:center;font-size:9.5px">www.pinebreezehvac.example</p>
  </article>

  <!-- Ad two -->
  <article class="ad ad-two">
    <svg class="bg-shapes" viewBox="0 0 328 328" aria-hidden="true">
      <circle cx="268" cy="100" r="118" fill="var(--white)"/>
      <path d="M0 214 C40 180 90 170 140 188 C180 200 200 180 230 150 L328 150 L328 328 L0 328Z" fill="var(--white)"/>
      <path d="M0 210 C40 176 90 166 140 184" fill="none" stroke="var(--pale-blue)" stroke-width="5"/>
    </svg>
    <div class="unit-photo" role="img" aria-label="Ceiling cassette and ductless wall-mounted air conditioning units on a blue splash" style="left:176px;top:14px;width:155px;height:170px"></div>
    <div class="spring" style="left:16px;top:0;font-size:52px;color:var(--white)">Spring</div>
    <div class="special" style="left:59px;top:76px;font-size:18px;color:var(--white)">SPECIAL</div>
    <p class="offer right" style="left:6px;top:104px;width:140px;color:var(--white)">New Central<br>Air conditioning or<br>Ductlesss air conditioning<br>installation.</p>
    <div class="badge" style="left:151px;top:158px;width:70px;height:70px"><span class="amount" style="font-size:19px">$750</span><span class="off" style="font-size:12px">OFF</span></div>
    <p class="right" style="left:6px;top:201px;width:137px;font-size:10px;line-height:12px">Our other special is a <b>$100</b><br>Central AC Tune up.</p>
    <p class="caps right" style="left:180px;top:184px;width:134px;font-size:13px">We provide</p>
    <p class="right" style="left:180px;top:196px;width:134px;font-family:'Montserrat',sans-serif;font-weight:900;font-size:22px;color:var(--orange)">24/7</p>
    <p class="caps right" style="left:180px;top:223px;width:134px;font-size:13px;line-height:16px">Emergency<br>Service</p>
    <p class="caps right" style="left:180px;top:264px;width:134px;font-size:12px">Free Estimates</p>
    <p class="right" style="left:180px;top:283px;width:134px;font-family:'Montserrat',sans-serif;font-weight:900;font-size:14px;color:var(--orange)">CALL US NOW</p>
    <p class="phone right" style="left:160px;top:299px;width:154px;font-size:17px">555-387-9042</p>
    <div class="brand" style="left:11px;top:240px"><span class="brand-dot" style="width:34px;height:34px"></span><span class="brand-name" style="font-size:18px">Silver Pine<br>Cooling</span></div>
    <p class="site" style="left:14px;top:304px;font-size:9.5px">www.pinebreezehvac.example</p>
  </article>

  <!-- Ad three -->
  <article class="ad ad-three">
    <svg class="bg-shapes" viewBox="0 0 328 328" aria-hidden="true">
      <path d="M0 0 L328 0 L328 60 C260 20 200 70 120 40 C70 22 30 30 0 45Z" fill="var(--pale-blue)"/>
      <path d="M0 18 C40 4 80 8 120 22 C180 44 240 10 328 30" fill="none" stroke="var(--sky-blue)" stroke-width="4" opacity=".6"/>
      <rect x="0" y="302" width="328" height="26" fill="var(--brand-blue)"/>
      <rect x="169" y="249" width="159" height="53" fill="var(--orange)"/>
    </svg>
    <div class="unit-photo" role="img" aria-label="Ceiling cassette and ductless wall-mounted air conditioning units on a blue splash" style="left:134px;top:6px;width:196px;height:140px"></div>
    <div class="spring" style="left:24px;top:58px;font-size:52px">Spring</div>
    <div class="special" style="left:66px;top:133px;font-size:18px">SPECIAL</div>
    <div class="badge" style="left:195px;top:116px;width:70px;height:70px"><span class="amount" style="font-size:19px">$750</span><span class="off" style="font-size:12px">OFF</span></div>
    <p class="offer" style="left:28px;top:161px;width:150px;line-height:16px">New Central<br>Air Conditioning or<br>Ductlesss Air Conditioning<br>Installation.</p>
    <p class="caps right" style="left:170px;top:205px;width:148px;font-size:12px">We provide <span style="font-size:21px;font-weight:400">24/7</span></p>
    <p class="caps right" style="left:170px;top:227px;width:148px;font-size:12px">Emergency service.</p>
    <div class="brand" style="left:12px;top:253px"><span class="brand-dot" style="width:30px;height:30px"></span><span class="brand-name" style="font-size:16px">Silver Pine<br>Cooling</span></div>
    <p class="caps" style="left:169px;width:159px;top:251px;text-align:center;font-size:11.5px">Free Estimates</p>
    <p class="phone" style="left:169px;width:159px;top:264px;text-align:center;font-size:17px;color:var(--white)">555-387-9042</p>
    <p class="site" style="left:169px;width:159px;top:287px;text-align:center;font-size:8px;color:var(--white)">www.pinebreezehvac.example</p>
    <p class="tune-up" style="left:0;width:328px;top:308px;text-align:center;font-size:9.5px;color:var(--white)">Our other special is a $100 Central AC Tune up.</p>
  </article>
</section>

<!-- Wide banner -->
<article class="banner">
  <svg style="left:0;top:0;width:1042px;height:334px" viewBox="0 0 1042 334" aria-hidden="true">
    <path d="M0 150 C150 60 320 70 480 130 C600 175 700 120 760 70 L760 0 L0 0Z" fill="var(--mist-blue)"/>
    <path d="M0 190 C160 100 330 110 500 170 C620 210 720 170 790 120 L790 240 C700 290 560 260 420 230 C260 196 120 200 0 250Z" fill="var(--pale-blue)" opacity=".75"/>
    <path d="M0 220 C160 150 320 160 480 200 C600 232 700 222 800 170" fill="none" stroke="var(--sky-blue)" stroke-width="6" opacity=".55"/>
  </svg>
  <div class="ceiling-photo" role="img" aria-label="Ceiling cassette central air conditioning unit" style="left:535px;top:14px;width:215px;height:122px"></div>
  <div class="unit-photo" role="img" aria-label="Ductless wall-mounted air conditioning unit with outdoor condenser on a blue splash" style="left:750px;top:12px;width:300px;height:245px"></div>
  <div class="spring" style="left:286px;top:-6px;font-size:94px">Spring</div>
  <div class="special" style="left:356px;top:120px;font-size:30px">SPECIAL</div>
  <div class="badge" style="left:686px;top:134px;width:140px;height:140px"><span class="amount" style="font-size:38px">$750</span><span class="off" style="font-size:24px">OFF</span></div>
  <div class="brand" style="left:28px;top:168px;gap:10px"><span class="brand-dot" style="width:60px;height:60px"></span><span class="brand-name" style="font-size:32px">Silver Pine<br>Cooling</span></div>
  <p class="right" style="left:330px;top:184px;width:314px;font-size:22px;line-height:27px">New Central Air Conditioning or Ductlesss Air Conditioning <b style="font-family:'Montserrat',sans-serif;font-style:italic;font-weight:900">Installation.</b></p>
  <p class="tune-up right" style="left:790px;top:222px;width:226px;font-style:normal;font-size:15.5px;line-height:19px">Our other<br>special is a $100<br>Central AC Tune up.</p>
  <p class="site" style="left:22px;top:256px;font-size:22px">www.pinebreezehvac.example</p>
  <p class="service-line">WE PROVIDE <span style="color:var(--orange);font-weight:900">24/7</span> EMERGENCY SERVICE.</p>
  <div class="estimate-band"></div>
  <p class="caps" style="left:537px;top:293px;font-size:24px;color:var(--white);text-transform:none">Free Estimates</p>
  <p class="phone" style="left:700px;top:288px;font-size:30px;color:var(--white)">Call 555-387-9042</p>
</article>

</body>
</html>
```